Stationary Design needed for Physical Therapy and Wellness Center

Letterhead, Envelopes, Business Cards (x2) needed. We are a studio specializing in helping our clients improve mobility, fitness, and recover from injury. We use the Velantric method and need to adhere to their trademark restrictions.
Updates

Target Market(s)

Potential Clients: active people...many from dance or athletic backgrounds.

Industry/Entity Type

Health And Wellness

Font styles to use
Sans Serif
Other font styles liked:
• Times New Roman for the word Velantric.

Colors
00a990
33b8a4
86cfc6
0393ce
33a6d7
85cae6

Requirements
Must have
• Attention to Velantric trademark guidelines (Times New Roman font, Bold type, use of registered trademark symbol). Examples of current stationary can be provided as an example.
• Concept of movement, flow.

```html
<!DOCTYPE html>
<html lang="en">
<head>
<meta charset="utf-8">
<title>flowmotive – Stationery Set</title>
<link href="https://fonts.googleapis.com/css2?family=Lato:wght@400;700&display=swap" rel="stylesheet">
<style>
  :root{
    --bg:#d1c6b2;
    --paper:#ffffff;
    --teal-dark:#00857c;
    --teal:#00bdb6;
    --teal-soft:#86cfc6;
    --ink:#222222;
    --grey:#666666;
    --sign:#d8dcef;
  }
  *{box-sizing:border-box;margin:0;padding:0}
  html,body{width:1200px;height:1200px;overflow:hidden}
  body{background:var(--bg);font-family:'Lato',sans-serif;color:var(--grey);position:relative}
  .sheet{position:absolute;background:var(--paper);overflow:hidden}
  .wave-band{position:absolute;left:0;bottom:0;width:100%;background:linear-gradient(180deg,var(--teal) 0%,var(--teal-soft) 100%)}
  .brand{font-family:'Lato',sans-serif;font-weight:400;color:var(--teal-dark);display:flex;align-items:center;gap:6px;line-height:1}
  .brand .dot{width:.55em;height:.55em;border-radius:50%;background:var(--teal-dark)}
  .contact{list-style:none}
  .contact li{display:flex;align-items:flex-start;gap:6px}
  .contact svg{flex:none;margin-top:.2em}

  /* Letterhead */
  .letterhead{left:50px;top:186px;width:499px;height:706px}
  .letterhead .brand{position:absolute;left:31px;top:76px;font-size:17px}
  .letterhead .contact{position:absolute;left:353px;top:54px;font-size:8.3px;line-height:10.2px}
  .letterhead .contact li.gap{margin-top:7px}
  .letter{position:absolute;left:31px;top:171px;width:432px;font-size:8.3px;line-height:10.9px}
  .letter .date{margin-bottom:10px}
  .letter .salutation{margin:27px 0 18px;color:var(--ink)}
  .letter p.body{text-align:justify;margin-bottom:6px}
  .sig-name{position:absolute;left:31px;top:490px;color:var(--ink);font-size:10px}
  .sig-role{position:absolute;left:31px;top:503px;font-size:8.3px}
  .sig-mark{position:absolute;left:31px;top:518px;width:86px;height:38px;background:var(--sign);border-radius:4px}
  .letterhead .wave-band{height:44px}

  /* Business card front */
  .card-front{left:560px;top:236px;width:218px;height:135px}
  .card-front .brand{position:absolute;left:20px;top:30px;font-size:11px}
  .card-front .person{position:absolute;left:176px;top:31px;font-size:5.6px;color:var(--ink);line-height:7px}
  .card-front .person span{display:block;color:var(--teal-dark)}
  .card-front .contact{position:absolute;left:20px;top:65px;font-size:5px;line-height:7.6px}
  .card-front .wave-band{height:20px}

  /* Business card back */
  .card-back{left:560px;top:388px;width:218px;height:135px;background:var(--teal-dark)}
  .card-back .brand{position:absolute;right:26px;top:58px;font-size:18px;color:#fff}
  .card-back .brand .dot{background:#fff}

  /* Envelope back */
  .envelope-back{left:579px;top:578px;width:486px;height:323px;background:transparent}
  .envelope-back svg{width:100%;height:100%;display:block}

  /* Envelope front */
  .envelope-front{left:668px;top:773px;width:485px;height:243px}
  .envelope-front .brand{position:absolute;left:43px;top:42px;font-size:20px}
  .envelope-front .contact{position:absolute;left:42px;top:112px;font-size:9.2px;line-height:12.6px}
  .envelope-front .contact li{margin-bottom:1.5px}
  .envelope-front .wave-band{height:44px}
</style>
</head>
<body>

<svg width="0" height="0" style="position:absolute" aria-hidden="true">
  <defs>
    <symbol id="i-phone" viewBox="0 0 10 10"><path d="M2 .5l2 2-1 1.2c.6 1.3 1.6 2.3 2.9 2.9L7.1 5.6l2 2L8 9.5C4 9.2.8 6 .5 2z" fill="#333"/></symbol>
    <symbol id="i-mail" viewBox="0 0 10 10"><rect x=".5" y="2" width="9" height="6.5" fill="#333"/><path d="M.5 2l4.5 3.6L9.5 2" stroke="#fff" stroke-width=".9" fill="none"/></symbol>
    <symbol id="i-web" viewBox="0 0 10 10"><circle cx="5" cy="5" r="4.2" fill="none" stroke="#333" stroke-width="1"/><path d="M.8 5h8.4M5 .8c-2 2.6-2 5.8 0 8.4M5 .8c2 2.6 2 5.8 0 8.4" stroke="#333" stroke-width=".8" fill="none"/></symbol>
    <symbol id="i-pin" viewBox="0 0 10 10"><path d="M5 .5a3.4 3.4 0 0 0-3.4 3.4C1.6 6.5 5 9.6 5 9.6s3.4-3.1 3.4-5.7A3.4 3.4 0 0 0 5 .5z" fill="#333"/><circle cx="5" cy="3.9" r="1.3" fill="#fff"/></symbol>
  </defs>
</svg>

<!-- Letterhead -->
<section class="sheet letterhead">
  <div class="brand"><span class="dot"></span>flowmotive</div>
  <ul class="contact">
    <li><svg width="7" height="7"><use href="#i-phone"/></svg>555-014-2290</li>
    <li><svg width="7" height="7"><use href="#i-mail"/></svg>info@flowmotivept.com</li>
    <li><svg width="7" height="7"><use href="#i-web"/></svg>www.flowmotivept.com</li>
    <li class="gap"><svg width="7" height="7"><use href="#i-pin"/></svg><span>4120 Linden Crest Road<br>Maple Heights, Ohio<br>44137</span></li>
  </ul>
  <div class="letter">
    <p class="date">18.09.2019</p>
    <p>Recipient name<br>72 Harlow Ave.<br>Fairview, PA 19370</p>
    <p class="salutation">Dear, Mr____________</p>
    <p class="body">Lorem Ipsum is simply dummy text of the printing and typesetting industry. Lorem Ipsum has been the industry's standard dummy text ever since the1500s,when an unknown printer took a galley of type and scrambled it to make a type specimen book. It has survived not only five centuries, but also the leap into electronic typesetting, remaining essentially unchanged.</p>
    <p class="body">Lorem Ipsum is simply dummy text of the printing and typesetting industry. Lorem Ipsum has been the industry's standard dummy text ever since the 1500s, when an unknown printer took a galley of type and scrambled it to make a type specimen book. It has survived not only five centuries, but also the leap into electronic typesetting, remaining essentially unchanged. It was popularised in the 1960s with the release of Brightleaf sheets containing Lorem Ipsum passages, and more recently with desktop publishing software like Pagewright Studio including versions of Lorem Ipsum.</p>
    <p class="body">Lorem Ipsum is simply dummy text of the printing and typesetting industry. Lorem Ipsum has been the industry's standard dummy text ever since the1500s.</p>
    <p class="body">Lorem Ipsum is simply dummy text of the printing and typesetting industry. Lorem Ipsum has been the industry's standard dummy text ever since the1500s,when an unknown printer took a galley of type and scrambled it to make a type specimen book.</p>
  </div>
  <p class="sig-name">YOUR NAME</p>
  <p class="sig-role">Designation</p>
  <div class="sig-mark" role="img" aria-label="Handwritten signature"></div>
  <div class="wave-band" role="img" aria-label="Decorative flowing teal band"></div>
</section>

<!-- Business card front -->
<section class="sheet card-front">
  <div class="brand"><span class="dot"></span>flowmotive</div>
  <p class="person">YOUR NAME<span>Designation</span></p>
  <ul class="contact">
    <li><svg width="5" height="5"><use href="#i-phone"/></svg>555-014-2290</li>
    <li><svg width="5" height="5"><use href="#i-mail"/></svg>info@flowmotivept.com</li>
    <li><svg width="5" height="5"><use href="#i-web"/></svg>www.flowmotivept.com</li>
    <li><svg width="5" height="5"><use href="#i-pin"/></svg><span>4120 Linden Crest Road Maple Heights,<br>Ohio 44137</span></li>
  </ul>
  <div class="wave-band" role="img" aria-label="Decorative flowing teal band"></div>
</section>

<!-- Business card back -->
<section class="sheet card-back">
  <div class="brand"><span class="dot"></span>flowmotive</div>
</section>

<!-- Envelope back -->
<section class="sheet envelope-back">
  <svg viewBox="0 0 486 323" aria-hidden="true">
    <rect x="0" y="80" width="486" height="243" fill="var(--paper)"/>
    <path d="M0 81 L10 8 Q11 0 20 0 L466 0 Q476 0 477 8 L486 81Z" fill="var(--teal-dark)"/>
    <path d="M0 81 L486 81 Q460 92 450 121 L35 121 Q25 92 0 81Z" fill="var(--teal)"/>
    <path d="M15 323 L20 132 Q22 121 35 121 L450 121 Q463 121 465 132 L470 323Z" fill="#fbfbfb" stroke="#e6e6e6" stroke-width="1"/>
  </svg>
</section>

<!-- Envelope front -->
<section class="sheet envelope-front">
  <div class="brand"><span class="dot"></span>flowmotive</div>
  <ul class="contact">
    <li><svg width="8" height="8"><use href="#i-phone"/></svg>555-014-2290</li>
    <li><svg width="8" height="8"><use href="#i-mail"/></svg>info@flowmotivept.com</li>
    <li><svg width="8" height="8"><use href="#i-web"/></svg>www.flowmotivept.com</li>
    <li><svg width="8" height="8"><use href="#i-pin"/></svg><span>4120 Linden Crest Road Maple Heights,<br>Ohio 44137</span></li>
  </ul>
  <div class="wave-band" role="img" aria-label="Decorative flowing teal band"></div>
</section>

</body>
</html>
```